Semaglutide Diet

A flyer design for a weight loss program based on the peptide Semaglutide that our clinic is rolling out. Here are some very rough ideas

```html
<!DOCTYPE html>
<html lang="en">
<head>
<meta charset="utf-8">
<title>Semaglutide Diet – Flyer</title>
<link rel="stylesheet" href="https://fonts.googleapis.com/css2?family=Anton&family=Arimo&family=Roboto+Condensed:wght@400;700&display=swap">
<style>
  :root {
    --page-bg: #e9e6e3;
    --flyer-bg: #111111;
    --accent-red: #d31a3e;
    --headline-brown: #8c6b5d;
    --ring-brown: #2e2620;
    --text-white: #ffffff;
  }
  html, body {
    margin: 0;
    padding: 0;
    width: 1200px;
    height: 1200px;
    overflow: hidden;
    background: var(--page-bg);
  }
  .flyer {
    position: absolute;
    left: 175px;
    top: 50px;
    width: 850px;
    height: 1100px;
    background: var(--flyer-bg);
    overflow: hidden;
    box-shadow: 0 6px 18px rgba(0,0,0,0.25);
  }
  .flyer-shapes {
    position: absolute;
    inset: 0;
    width: 850px;
    height: 1100px;
  }
  .brand-name {
    position: absolute;
    left: 60px;
    top: 86px;
    margin: 0;
    font-family: "Anton", "Oswald", sans-serif;
    font-weight: 400;
    font-size: 60px;
    line-height: 70px;
    color: var(--text-white);
    text-transform: uppercase;
  }
  .headline {
    position: absolute;
    left: 60px;
    top: 244px;
    margin: 0;
    font-family: "Anton", "Oswald", sans-serif;
    font-weight: 400;
    font-size: 86px;
    line-height: 91px;
    color: var(--headline-brown);
    text-transform: uppercase;
  }
  .benefits {
    position: absolute;
    left: 60px;
    top: 540px;
    margin: 0;
    padding: 0;
    list-style: none;
    font-family: "Arimo", Arial, sans-serif;
    font-size: 27px;
    color: var(--text-white);
  }
  .benefits li {
    position: relative;
    padding-left: 28px;
    height: 47.3px;
    line-height: 34px;
  }
  .benefits li::before {
    content: "";
    position: absolute;
    left: 2px;
    top: 14px;
    width: 9px;
    height: 9px;
    border-radius: 50%;
    background: var(--text-white);
  }
  .contact {
    position: absolute;
    right: 39px;
    top: 874px;
    text-align: right;
    font-family: "Roboto Condensed", "Arial Narrow", sans-serif;
    color: var(--text-white);
    font-size: 18.5px;
    line-height: 22px;
  }
  .contact h2 {
    margin: 0 0 5px;
    font-size: 21px;
    font-weight: 700;
    text-transform: uppercase;
  }
  .contact p {
    margin: 0 0 5px;
  }
</style>
</head>
<body>
  <main class="flyer">
    <svg class="flyer-shapes" viewBox="0 0 850 1100" xmlns="http://www.w3.org/2000/svg">
      <defs>
        <linearGradient id="grad-workout" x1="0" y1="0" x2="1" y2="1">
          <stop offset="0" stop-color="#e8e9ea"/>
          <stop offset="0.6" stop-color="#9a9c9f"/>
          <stop offset="1" stop-color="#3b3d41"/>
        </linearGradient>
        <linearGradient id="grad-waist" x1="0" y1="0" x2="0" y2="1">
          <stop offset="0" stop-color="#f2f0ef"/>
          <stop offset="0.55" stop-color="#d9a98a"/>
          <stop offset="1" stop-color="#27a9d8"/>
        </linearGradient>
        <linearGradient id="grad-cardio" x1="0" y1="0" x2="1" y2="1">
          <stop offset="0" stop-color="#e5e7ea"/>
          <stop offset="1" stop-color="#4a4c50"/>
        </linearGradient>
      </defs>

      <!-- top-left chevrons -->
      <g class="chevrons" fill="var(--accent-red)">
        <polygon points="5,0 23,0 51,29 23,58 5,58 33,29"/>
        <polygon points="42,0 60,0 88,29 60,58 42,58 70,29"/>
        <polygon points="79,0 97,0 125,29 97,58 79,58 107,29"/>
      </g>

      <!-- main workout photo in red ring -->
      <circle class="ring-main" cx="631" cy="275" r="256" fill="var(--accent-red)"/>
      <g role="img" aria-label="Photo of two women doing a cardio workout in a bright gym">
        <circle cx="631" cy="275" r="218" fill="url(#grad-workout)"/>
      </g>

      <!-- waist measuring photo in red ring -->
      <circle class="ring-small" cx="731" cy="687" r="141" fill="var(--accent-red)"/>
      <g role="img" aria-label="Photo of a woman measuring her waist with a tape measure">
        <circle cx="731" cy="687" r="121" fill="url(#grad-waist)"/>
      </g>

      <!-- gym equipment photo in brown arc -->
      <circle class="ring-arc" cx="287" cy="1100" r="303" fill="var(--ring-brown)"/>
      <g role="img" aria-label="Photo of a row of treadmills and elliptical machines in a gym">
        <circle cx="287" cy="1100" r="266" fill="url(#grad-cardio)"/>
      </g>

      <!-- bottom-right stripes -->
      <g class="stripes" fill="var(--accent-red)">
        <polygon points="600,1100 617,1100 647,1058 630,1058"/>
        <polygon points="629,1100 646,1100 676,1058 659,1058"/>
        <polygon points="658,1100 675,1100 705,1058 688,1058"/>
        <polygon points="687,1100 704,1100 734,1058 717,1058"/>
        <polygon points="716,1100 733,1100 763,1058 746,1058"/>
        <polygon points="745,1100 762,1100 792,1058 775,1058"/>
        <polygon points="774,1100 791,1100 821,1058 804,1058"/>
        <polygon points="803,1100 820,1100 850,1058 833,1058"/>
        <polygon points="832,1100 849,1100 850,1098 850,1076"/>
      </g>
    </svg>

    <p class="brand-name">Your Logo<br>Here</p>

    <h1 class="headline">Do You<br>Want<br>Result?</h1>

    <ul class="benefits">
      <li>Lose 5 pounds or more</li>
      <li>Improve your metabolism</li>
      <li>Have more energy</li>
      <li>Lose water weight</li>
      <li>Improve overall health</li>
    </ul>

    <section class="contact">
      <h2>Contact Us</h2>
      <p>Email : yourname@website.com</p>
      <p>Ph.No. : 0123 456789</p>
      <p>123, Area Name, City Name,<br>State Name, Country Name,<br>Country Code.</p>
    </section>
  </main>
</body>
</html>
```